Corporate consulting business needs a business card

I want a professional business card.... surprise me

Updates

Reason: i dont think 2 days is enough

Target Market(s)

Corprorate and Not for Profit firms and organisations

Industry/Entity Type

Consulting

Contact Information for Business Card

Logo
Corporate Consulting Services
On Time, On Budget, Beyond Expectation
Tovan Presfield
Director
0427 31 94 62 (Larger)
tovan@tp-advisory.com.au
www.tp-advisory.com.au
include little icons beside the contact info:

- Envelope = email
- Phone = phone
- Globe = website

Font styles to use
Serif
Sans Serif

Requirements
Must have
• Professional and clean
Nice to have
• you tell me

```html
<!DOCTYPE html>
<html lang="en">
<head>
<meta charset="utf-8">
<title>Presfield Advisory – Business Card</title>
<link href="https://fonts.googleapis.com/css2?family=Lato:wght@400;700&display=swap" rel="stylesheet">
<style>
  :root {
    --backdrop: #84a7bf;
    --accent-blue: #7fa3bd;
    --badge-blue: #93b4cb;
    --brand-brown: #5a2e14;
    --ink: #111111;
    --card-white: #f4f4f4;
    --header-top: #fafafa;
    --header-bottom: #e2e2e2;
  }
  html, body {
    margin: 0;
    width: 1200px;
    height: 1200px;
    overflow: hidden;
    background: var(--backdrop);
  }
  .stage {
    position: relative;
    width: 1200px;
    height: 1200px;
  }
  .card {
    position: absolute;
    top: 300px;
    width: 389px;
    height: 600px;
    overflow: hidden;
    background: var(--card-white);
    box-shadow: 0 6px 18px rgba(30, 55, 75, 0.28);
  }
  .card--front { left: 162px; }
  .card--back { left: 650px; }
  .card__art {
    position: absolute;
    inset: 0;
    width: 100%;
    height: 100%;
  }
  .brand {
    position: absolute;
    top: 0;
    left: 0;
    width: 100%;
    height: 114px;
    display: flex;
    align-items: center;
    justify-content: center;
    gap: 12px;
  }
  .brand__mark {
    width: 16px;
    height: 16px;
    background: var(--brand-brown);
    flex: none;
  }
  .brand__name {
    margin: 0;
    font-family: "Lato", sans-serif;
    font-weight: 700;
    font-size: 30px;
    letter-spacing: 0.5px;
    color: var(--brand-brown);
    line-height: 1;
    white-space: nowrap;
  }
  .person {
    position: absolute;
    left: 176px;
    top: 330px;
    width: 200px;
    text-align: center;
    font-family: "Lato", sans-serif;
    font-weight: 700;
    font-size: 24px;
    line-height: 31px;
    color: var(--ink);
    white-space: nowrap;
  }
  .person__icon {
    display: block;
    width: 44px;
    height: 44px;
    margin: 0 auto 8px;
  }
  .contacts {
    position: absolute;
    left: 36px;
    top: 462px;
    margin: 0;
    padding: 0;
    list-style: none;
    font-family: "Lato", sans-serif;
    color: var(--ink);
  }
  .contacts__item {
    display: flex;
    align-items: center;
    gap: 10px;
    white-space: nowrap;
  }
  .contacts__icon { width: 28px; height: 28px; flex: none; }
  .contacts__item--phone { font-size: 46px; height: 54px; gap: 6px; }
  .contacts__item--mail, .contacts__item--web { font-size: 23px; height: 36px; margin-top: 2px; }
  .tagline {
    position: absolute;
    right: 44px;
    top: 384px;
    margin: 0;
    padding: 0;
    list-style: none;
    font-family: "Lato", sans-serif;
    font-size: 24px;
    color: var(--ink);
  }
  .tagline__item {
    display: flex;
    justify-content: flex-end;
    align-items: center;
    gap: 12px;
    height: 48px;
  }
  .tagline__badge {
    width: 26px;
    height: 26px;
    border-radius: 50%;
    background: var(--badge-blue);
    box-shadow: inset 0 0 0 2px var(--badge-blue), inset 0 0 0 4px #ffffff;
    flex: none;
  }
</style>
</head>
<body>
<main class="stage">

  <section class="card card--front" aria-label="Business card front">
    <svg class="card__art" viewBox="0 0 486 750" preserveAspectRatio="none">
      <defs>
        <linearGradient id="header-fill" x1="0" y1="0" x2="0" y2="1">
          <stop offset="0" stop-color="#fafafa"/>
          <stop offset="1" stop-color="#e2e2e2"/>
        </linearGradient>
        <linearGradient id="front-photo" x1="0" y1="0" x2="1" y2="0.4">
          <stop offset="0" stop-color="#0e2238"/>
          <stop offset="0.35" stop-color="#6c6c6c"/>
          <stop offset="0.6" stop-color="#8a8a8a"/>
          <stop offset="0.85" stop-color="#3d6a93"/>
          <stop offset="1" stop-color="#c9d6e2"/>
        </linearGradient>
        <radialGradient id="panel-fill" cx="0.5" cy="0.45" r="0.7">
          <stop offset="0" stop-color="#ffffff"/>
          <stop offset="1" stop-color="#e4e4e4"/>
        </radialGradient>
      </defs>
      <rect x="0" y="0" width="486" height="143" fill="url(#header-fill)"/>
      <rect x="0" y="143" width="486" height="17" fill="#7fa3bd"/>
      <rect x="0" y="160" width="486" height="590" fill="url(#front-photo)" role="img" aria-label="Photo of a businessman in a grey suit reaching out for a handshake"/>
      <polygon points="0,520 291,337 486,455 486,750 0,750" fill="#7fa3bd"/>
      <polygon points="0,548 291,362 486,480 486,750 0,750" fill="url(#panel-fill)"/>
    </svg>

    <header class="brand">
      <span class="brand__mark"></span>
      <h1 class="brand__name">Presfield Advisory</h1>
    </header>

    <div class="person">
      <svg class="person__icon" viewBox="0 0 44 44" aria-hidden="true">
        <circle cx="22" cy="22" r="22" fill="#111111"/>
        <circle cx="22" cy="17" r="6" fill="#ffffff"/>
        <path d="M12 31 q10 -12 20 0 z" fill="#ffffff"/>
      </svg>
      <div class="person__name">Tovan Presfield</div>
      <div class="person__role">Director</div>
    </div>

    <ul class="contacts">
      <li class="contacts__item contacts__item--phone">
        <svg class="contacts__icon" viewBox="0 0 28 28" aria-hidden="true">
          <circle cx="14" cy="14" r="14" fill="#111111"/>
          <rect x="9" y="6" width="10" height="16" rx="2" fill="#ffffff"/>
          <rect x="11" y="8.5" width="6" height="10" fill="#111111"/>
        </svg>
        <span>0427 31 94 62</span>
      </li>
      <li class="contacts__item contacts__item--mail">
        <svg class="contacts__icon" viewBox="0 0 28 28" aria-hidden="true">
          <circle cx="14" cy="14" r="14" fill="#111111"/>
          <rect x="7" y="9" width="14" height="10" rx="1" fill="#ffffff"/>
          <path d="M7 9.5 L14 15 L21 9.5" stroke="#111111" stroke-width="1.6" fill="none"/>
        </svg>
        <span>tovan@tp-advisory.com.au</span>
      </li>
      <li class="contacts__item contacts__item--web">
        <svg class="contacts__icon" viewBox="0 0 28 28" aria-hidden="true">
          <circle cx="14" cy="14" r="14" fill="#111111"/>
          <g stroke="#ffffff" stroke-width="1.3" fill="none">
            <circle cx="14" cy="14" r="7.5"/>
            <ellipse cx="14" cy="14" rx="3.5" ry="7.5"/>
            <line x1="6.5" y1="14" x2="21.5" y2="14"/>
            <line x1="8" y1="10" x2="20" y2="10"/>
            <line x1="8" y1="18" x2="20" y2="18"/>
          </g>
        </svg>
        <span>www.tp-advisory.com.au</span>
      </li>
    </ul>
  </section>

  <section class="card card--back" aria-label="Business card back">
    <svg class="card__art" viewBox="0 0 486 750" preserveAspectRatio="none">
      <defs>
        <linearGradient id="header-fill-b" x1="0" y1="0" x2="0" y2="1">
          <stop offset="0" stop-color="#fafafa"/>
          <stop offset="1" stop-color="#e2e2e2"/>
        </linearGradient>
        <linearGradient id="back-photo" x1="0" y1="0" x2="1" y2="0">
          <stop offset="0" stop-color="#e8ecef"/>
          <stop offset="0.12" stop-color="#dde2e6"/>
          <stop offset="0.3" stop-color="#22345a"/>
          <stop offset="0.5" stop-color="#2b3f66"/>
          <stop offset="0.75" stop-color="#22345a"/>
          <stop offset="0.9" stop-color="#e3e7ea"/>
          <stop offset="1" stop-color="#f0f2f4"/>
        </linearGradient>
        <radialGradient id="panel-fill-b" cx="0.5" cy="0.45" r="0.7">
          <stop offset="0" stop-color="#ffffff"/>
          <stop offset="1" stop-color="#e4e4e4"/>
        </radialGradient>
      </defs>
      <rect x="0" y="0" width="486" height="143" fill="url(#header-fill-b)"/>
      <rect x="0" y="143" width="486" height="17" fill="#7fa3bd"/>
      <rect x="0" y="160" width="486" height="590" fill="url(#back-photo)" role="img" aria-label="Photo of a businessman in a navy suit holding a clipboard"/>
      <polygon points="0,575 290,337 486,455 486,750 0,750" fill="#7fa3bd"/>
      <polygon points="0,600 290,362 486,480 486,750 0,750" fill="url(#panel-fill-b)"/>
    </svg>

    <header class="brand">
      <span class="brand__mark"></span>
      <h2 class="brand__name">Presfield Advisory</h2>
    </header>

    <ul class="tagline">
      <li class="tagline__item"><span>On Time</span><span class="tagline__badge"></span></li>
      <li class="tagline__item"><span>On Budget</span><span class="tagline__badge"></span></li>
      <li class="tagline__item"><span>Beyond Expectation</span><span class="tagline__badge"></span></li>
    </ul>
  </section>

</main>
</body>
</html>
```